High Quality Business card for Property Management Agency - Super Classy and professional design

High Quality Business card design.

We need a business card designed for our Property Management Agency.
We are located on Sydney's Northern Beaches and manage beautiful properties along the beach and harbor.
We need a design that oozes modern, classy and professional.
I would like it to be double sided with contact details and logo on the front and just the logo on the back.

I need a print ready PDF version of the file as well as an editable photoshop (PSD) version of the file.

Logo and information details attached.

Target Market(s)

Property owners/investors, Male and Female Aged 28-65

Industry/Entity Type

Real Estate

Contact Information for Business Card

Tom Carrick
Tel: 0467 239 018
Email: tom@harvestlaneestates.com.au
Website: www.harvestlaneestates.com.au
Address: Level 2, 17 Wattlecourt Rd, Dunmarra NSW 2187

Font styles to use
Sans Serif

Requirements
Must have
• - Logo front and back
• - Business card details listed above and attached
• - Colour
Nice to have
• Sleek and professional

```html
<!DOCTYPE html>
<html lang="en">
<head>
<meta charset="utf-8">
<title>Harvest Lane Estates – Business Card</title>
<link rel="stylesheet" href="https://fonts.googleapis.com/css2?family=Open+Sans:wght@400;600&family=Montserrat:wght@800&family=Lato:wght@400&display=swap">
<style>
  :root {
    --page: #e6e4e1;
    --charcoal: #2b2b2b;
    --slate: #4f4c4a;
    --blue: #1e96d2;
    --paper: #f1f1f1;
    --ink: #262626;
    --white: #ffffff;
  }
  * { box-sizing: border-box; margin: 0; padding: 0; }
  html, body { width: 1200px; height: 800px; overflow: hidden; }
  body { background: var(--page); position: relative; font-family: "Lato", sans-serif; }

  .card {
    position: absolute; left: 320px; width: 560px; height: 320px;
    overflow: hidden; border-radius: 4px;
    box-shadow: 0 6px 18px rgba(0,0,0,.18);
  }
  .card-shapes { position: absolute; inset: 0; width: 100%; height: 100%; }

  /* Back side */
  .card-back { top: 50px; background: var(--charcoal); }
  .card-back .brand { position: absolute; left: 40px; top: 128px; color: var(--white); font-family: "Open Sans", sans-serif; font-weight: 600; }
  .card-back .brand-name { font-size: 48px; letter-spacing: .5px; line-height: 1; }
  .card-back .brand-sub { font-size: 15px; margin: 6px 0 0 322px; letter-spacing: 1px; }

  /* Front side */
  .card-front { top: 420px; background: var(--paper); }
  .card-front .brand { position: absolute; left: 30px; top: 38px; color: var(--white); font-family: "Open Sans", sans-serif; font-weight: 600; }
  .card-front .brand-name { font-size: 25px; line-height: 1; }
  .card-front .brand-sub { font-size: 8px; margin: 3px 0 0 172px; letter-spacing: .8px; }

  .holder-name {
    position: absolute; left: 330px; top: 112px;
    font-family: "Montserrat", sans-serif; font-weight: 800;
    font-size: 22px; color: var(--ink); letter-spacing: .3px;
  }

  .contact { position: absolute; top: 198px; text-align: center; color: var(--ink); font-size: 11px; line-height: 1.35; }
  .contact svg { display: block; margin: 0 auto 10px; width: 26px; height: 26px; }
  .contact-address { left: 55px; width: 190px; }
  .contact-phone { left: 250px; width: 110px; }
  .contact-online { left: 355px; width: 200px; font-size: 10.5px; }
</style>
</head>
<body>

<section class="card card-back" aria-label="Business card back">
  <svg class="card-shapes" viewBox="0 0 560 320" preserveAspectRatio="none" aria-hidden="true">
    <polygon points="150,0 560,0 560,40 375,128" fill="var(--slate)"/>
    <polygon points="488,88 560,52 560,138" fill="var(--blue)"/>
  </svg>
  <div class="brand">
    <div class="brand-name">HARVEST LANE</div>
    <div class="brand-sub">ESTATES</div>
  </div>
</section>

<section class="card card-front" aria-label="Business card front">
  <svg class="card-shapes" viewBox="0 0 560 320" preserveAspectRatio="none" aria-hidden="true">
    <polygon points="0,0 300,0 172,180 0,140" fill="var(--slate)"/>
    <polygon points="296,0 560,0 560,30 412,98" fill="var(--blue)"/>
  </svg>
  <div class="brand">
    <div class="brand-name">HARVEST LANE</div>
    <div class="brand-sub">ESTATES</div>
  </div>

  <div class="holder-name">TOM CARRICK</div>

  <div class="contact contact-address">
    <svg viewBox="0 0 24 24" fill="none" stroke="var(--blue)" stroke-width="1.6" aria-hidden="true">
      <path d="M12 22s7-7.2 7-12.5A7 7 0 0 0 5 9.5C5 14.8 12 22 12 22z"/>
      <circle cx="12" cy="9.5" r="2.6"/>
    </svg>
    Level 2, 17 Wattlecourt Rd,<br>Dunmarra NSW 2187
  </div>

  <div class="contact contact-phone">
    <svg viewBox="0 0 24 24" fill="none" stroke="var(--blue)" stroke-width="1.6" aria-hidden="true">
      <rect x="6.5" y="2.5" width="11" height="19" rx="1.8"/>
      <line x1="10.5" y1="18.5" x2="13.5" y2="18.5"/>
    </svg>
    0467 239 018
  </div>

  <div class="contact contact-online">
    <svg viewBox="0 0 24 24" fill="none" stroke="var(--blue)" stroke-width="1.6" aria-hidden="true">
      <rect x="2.5" y="5" width="19" height="14" rx="1"/>
      <polyline points="2.5,5.5 12,13 21.5,5.5"/>
    </svg>
    www.harvestlaneestates.com.au<br>tom@harvestlaneestates.com.au
  </div>
</section>

</body>
</html>
```